Urgent Flyer needed - Term 1 begins

I am looking for a flyer design - double sided half A4 full colour. Bright Sprouts Enriched Learning Centre is in Dubai and runs a program for children aged from 6 months to 6 years old. Please see our website and Facebook page for more info on the brand and service. www.facebook.com/brightsprouts and www.brightsprouts.ae
We are also offering a free class voucher so i thought something creative like a vintage coupon or a golden ticket style design could work well... I also like the idea of something like a happy bunch of kids learning as a background image in black and white and then BRIGHT SPROUTS in our colours with our contact details and then on the reverse side a bit of text, and the free class info...

```html
<!DOCTYPE html>
<html lang="en">
<head>
<meta charset="utf-8">
<title>Bright Sprouts Flyer – Back</title>
<link href="https://fonts.googleapis.com/css2?family=Baloo+2:wght@500;600;700;800&display=swap" rel="stylesheet">
<style>
  :root{
    --page-bg:#2b2a29;
    --blue-light:#6db6cf;
    --blue:#4f9fbd;
    --blue-deep:#3a88a7;
    --band:#3e7f99;
    --orange:#f4891f;
    --shadow-blue:#2c6f8a;
    --panel:#def0f8;
    --ink-blue:#2e80a5;
    --white:#ffffff;
    --photo-warm:#b98a6a;
    --photo-bright:#e9c9b8;
  }
  *{box-sizing:border-box;margin:0;padding:0}
  html,body{width:1200px;height:1000px;overflow:hidden}
  body{background:var(--page-bg);font-family:"Baloo 2",system-ui,sans-serif;position:relative}

  .flyer{
    position:absolute;left:268px;top:30px;width:664px;height:940px;
    background:linear-gradient(180deg,var(--blue-light) 0%,var(--blue) 45%,var(--blue-deep) 100%);
    overflow:hidden;
    box-shadow:0 10px 30px rgba(0,0,0,.5);
  }
  .corner{position:absolute;left:0;top:0}

  .intro{
    position:absolute;left:46px;top:30px;width:578px;
    color:var(--white);font-weight:700;font-size:19px;line-height:24px;
    text-align:justify;
  }
  .intro p:first-child{text-indent:70px}
  .intro p+p{margin-top:14px}

  .topics{
    position:absolute;left:0;top:318px;width:440px;height:190px;
    background:var(--band);
    padding:20px 24px 0 34px;color:var(--white);
  }
  .topics h2{font-size:25px;font-weight:800;letter-spacing:.5px;line-height:28px}
  .topics p{font-size:16px;font-weight:700;line-height:20px;margin-top:4px}

  .voucher{position:absolute;right:0;top:298px;width:232px;height:124px;z-index:2}
  .voucher-shadow{position:absolute;left:10px;top:14px;width:222px;height:110px;background:var(--shadow-blue)}
  .voucher-card{
    position:absolute;left:0;top:0;width:232px;height:110px;background:var(--orange);
    color:var(--white);text-align:center;font-weight:800;
    display:flex;flex-direction:column;justify-content:center;
    box-shadow:0 3px 6px rgba(0,0,0,.25);
  }
  .voucher-card .big{font-size:36px;line-height:34px}
  .voucher-card .small{font-size:23px;line-height:24px}

  .photo{position:absolute;background:var(--white);padding:7px;box-shadow:0 4px 10px rgba(0,0,0,.35)}
  .photo .fill{width:100%;height:100%}
  .photo-one{left:58px;top:522px;width:330px;height:228px;z-index:1}
  .photo-one .fill{background:linear-gradient(160deg,#8a5a3a 0%,var(--photo-warm) 50%,#3f78b8 100%)}
  .photo-two{left:360px;top:462px;width:300px;height:212px;z-index:2}
  .photo-two .fill{background:linear-gradient(135deg,#f3e6dc 0%,var(--photo-bright) 50%,#c98f62 100%)}

  .tab-orange{position:absolute;right:0;top:676px}

  .footer{
    position:absolute;left:0;bottom:0;width:664px;height:178px;background:var(--white);z-index:3;
  }
  .brand{
    position:absolute;left:22px;top:16px;width:168px;height:146px;
    border:2px solid var(--panel);
    display:flex;flex-direction:column;align-items:center;justify-content:center;gap:10px;
  }
  .brand-dot{width:46px;height:46px;border-radius:50%;background:var(--orange)}
  .brand-name{color:var(--ink-blue);font-weight:700;font-size:19px;line-height:20px;text-align:center}
  .contact{
    position:absolute;left:208px;top:16px;width:436px;height:146px;background:var(--panel);
    padding:10px 18px;color:var(--ink-blue);
  }
  .contact h3{
    color:var(--orange);font-size:22px;font-weight:800;line-height:26px;
    display:inline-block;border-bottom:2px solid var(--orange);
  }
  .contact .line{font-size:17px;font-weight:500;line-height:22px}
  .contact .icon-line{display:flex;align-items:center;gap:10px;margin-top:3px}
  .site{
    position:absolute;right:20px;bottom:2px;color:var(--ink-blue);
    font-weight:800;font-size:17px;
  }
</style>
</head>
<body>
<main class="flyer">
  <svg class="corner" width="100" height="76" viewBox="0 0 100 76" aria-hidden="true">
    <polygon points="0,0 100,0 0,62" fill="#f4891f"/>
    <polygon points="0,62 100,0 100,9 0,75" fill="#ffffff"/>
  </svg>

  <section class="intro">
    <p>Our accelerated learning classes are for children aged from 6 months to 6 years. Classes are 60 minutes in length and we request a parent attend the class with the child.</p>
    <p>Each level of the program has been carefully designed so that the activities are progressive and consistency is key. We recommend your child attend the centre for a minimum of one session per week, however we do encourage as much exposure to right brain stimulation and enriched learning as possible during this key stage of brain development.</p>
  </section>

  <section class="topics">
    <h2>CLASS TOPIC INCLUDES -</h2>
    <p>Focus &amp; Concentration, Numeracy, Literacy, Observation, Speech Development, Memory, Critical Thinking, Image Training, Intuitive Play, Flashcards, Sign Language and Music Awareness.</p>
  </section>

  <div class="voucher">
    <div class="voucher-shadow"></div>
    <div class="voucher-card">
      <span class="big">Free</span>
      <span class="small">Class Voucher</span>
      <span class="small">Available</span>
    </div>
  </div>

  <figure class="photo photo-one"><div class="fill" role="img" aria-label="Photo of a young girl at a classroom table with a learning board"></div></figure>
  <figure class="photo photo-two"><div class="fill" role="img" aria-label="Photo of children painting with a teacher in a bright classroom"></div></figure>

  <svg class="tab-orange" width="250" height="80" viewBox="0 0 250 80" aria-hidden="true">
    <polygon points="250,0 250,80 0,55" fill="#f4891f"/>
  </svg>

  <footer class="footer">
    <div class="brand">
      <span class="brand-dot"></span>
      <span class="brand-name">BRIGHT SPROUTS</span>
    </div>
    <div class="contact">
      <h3>CONTACT US -</h3>
      <p class="line">Bright Sprouts Enriched Learning Centre</p>
      <p class="line">Unit 14, Block C, Meadow Park, Dubai</p>
      <p class="line icon-line">
        <svg width="26" height="20" viewBox="0 0 26 20" aria-hidden="true"><path d="M2 6 Q13 -2 24 6 L21 9 L17 7 L17 5 Q13 3 9 5 L9 7 L5 9 Z" fill="#2e80a5"/><rect x="6" y="10" width="14" height="9" rx="2" fill="#2e80a5"/></svg>
        +971 45550192 / +971 555550147
      </p>
      <p class="line icon-line">
        <svg width="26" height="18" viewBox="0 0 26 18" aria-hidden="true"><rect x="1" y="1" width="24" height="16" fill="#2e80a5"/><polyline points="1,1 13,10 25,1" fill="none" stroke="#def0f8" stroke-width="2"/></svg>
        register@brightsprouts.ae
      </p>
    </div>
    <div class="site">www.brightsprouts.ae</div>
  </footer>
</main>
</body>
</html>
```